International tradind company needs a professional Business Card

We are an international trading company and we need a business card for our CEO and employers so they can give it away in their meetings and while networking.
We want the card design quality to cause an immediate "wow" and we count on you to do that!

key-words and concepts to communicate: trustworthiness, ethics, sucess, modern, global business, networking

Our favorite colours are blue and grey but we are open to suggestions.

It would be recommended that our logo was part of the card. You can see it in www.veldoranexus.com . We also would like the following info on the card:
Name
position in the company
cell phone and personal email

Industry/Entity Type

Business

```html
<!DOCTYPE html>
<html lang="en">
<head>
<meta charset="utf-8">
<title>Veldora Nexus – Business Card</title>
<link rel="stylesheet" href="https://fonts.googleapis.com/css2?family=Open+Sans:wght@400;600&family=Oswald:wght@300;600&display=swap">
<style>
  :root {
    --page-bg: #e6e8ee;
    --card-white: #ffffff;
    --card-silver: #dcdde8;
    --indigo-deep: #2b2f86;
    --indigo-mid: #4d52a8;
    --indigo-soft: #8c8fc8;
    --ink: #1f2160;
    --accent-blue: #3b6fb6;
    --shadow: rgba(30, 34, 90, 0.25);
  }
  * { margin: 0; padding: 0; box-sizing: border-box; }
  html, body {
    width: 1200px;
    height: 873px;
    overflow: hidden;
    background: var(--page-bg);
  }
  .sheet {
    width: 1200px;
    height: 873px;
    display: flex;
    align-items: center;
    justify-content: center;
    gap: 60px;
  }
  .card {
    position: relative;
    width: 520px;
    height: 300px;
    border-radius: 4px;
    overflow: hidden;
    background: linear-gradient(100deg, var(--card-silver) 0%, var(--card-white) 35%, var(--card-white) 60%, var(--card-silver) 100%);
    box-shadow: 0 12px 30px var(--shadow);
  }
  .card-shape {
    position: absolute;
    inset: 0;
    width: 100%;
    height: 100%;
  }
  .brand {
    display: flex;
    align-items: center;
    gap: 12px;
  }
  .brand-mark {
    width: 34px;
    height: 34px;
    border-radius: 50%;
    background: var(--indigo-mid);
    flex: none;
  }
  .brand-name {
    font-family: "Open Sans", sans-serif;
    font-weight: 400;
    font-size: 30px;
    line-height: 1;
    color: var(--ink);
  }
  .brand-tagline {
    font-family: "Open Sans", sans-serif;
    font-size: 13px;
    color: var(--accent-blue);
    margin-top: 4px;
  }
  .brand-web {
    font-family: "Open Sans", sans-serif;
    font-size: 12px;
    color: var(--accent-blue);
    margin-top: 4px;
  }

  /* Front: personal details */
  .card-front .content {
    position: absolute;
    left: 40px;
    top: 30px;
  }
  .card-front .brand-text { margin-bottom: 18px; }
  .holder-name {
    font-family: "Oswald", sans-serif;
    font-weight: 600;
    font-size: 24px;
    letter-spacing: 0.5px;
    color: var(--indigo-deep);
    text-transform: uppercase;
  }
  .holder-name .surname { font-weight: 300; }
  .holder-detail {
    font-family: "Oswald", sans-serif;
    font-weight: 300;
    font-size: 18px;
    color: var(--accent-blue);
    line-height: 1.35;
  }

  /* Back: brand side */
  .card-back .content {
    position: absolute;
    right: 40px;
    top: 110px;
  }
</style>
</head>
<body>
<main class="sheet">

  <article class="card card-front">
    <svg class="card-shape" viewBox="0 0 520 300" aria-hidden="true">
      <defs>
        <linearGradient id="frontBand" x1="0" y1="0" x2="1" y2="0">
          <stop offset="0" stop-color="#8c8fc8"/>
          <stop offset="0.5" stop-color="#2b2f86"/>
          <stop offset="1" stop-color="#4d52a8"/>
        </linearGradient>
      </defs>
      <path d="M0 300 L0 262 C160 262 330 250 520 118 L520 300 Z" fill="#f2f2f6"/>
      <path d="M0 300 L0 276 C170 276 345 262 520 140 L520 300 Z" fill="url(#frontBand)"/>
    </svg>
    <div class="content">
      <div class="brand">
        <span class="brand-mark"></span>
        <div class="brand-text">
          <div class="brand-name">Veldora Nexus</div>
          <div class="brand-tagline">Business Services</div>
        </div>
      </div>
      <div class="holder-name">Your <span class="surname">Fullname</span></div>
      <div class="holder-detail">Your Position</div>
      <div class="holder-detail">Your Email</div>
    </div>
  </article>

  <article class="card card-back">
    <svg class="card-shape" viewBox="0 0 520 300" aria-hidden="true">
      <defs>
        <linearGradient id="backBand" x1="0" y1="0" x2="1" y2="1">
          <stop offset="0" stop-color="#2b2f86"/>
          <stop offset="0.6" stop-color="#4d52a8"/>
          <stop offset="1" stop-color="#8c8fc8"/>
        </linearGradient>
      </defs>
      <path d="M0 0 L360 0 C250 30 210 110 190 190 C175 250 100 300 0 300 Z" fill="#f2f2f6"/>
      <path d="M0 0 L335 0 C235 32 195 110 176 186 C162 240 90 290 0 290 Z" fill="url(#backBand)"/>
    </svg>
    <div class="content">
      <div class="brand">
        <span class="brand-mark"></span>
        <div class="brand-text">
          <div class="brand-name">Veldora Nexus</div>
          <div class="brand-tagline">Business Services</div>
          <div class="brand-web">www.veldoranexus.com</div>
        </div>
      </div>
    </div>
  </article>

</main>
</body>
</html>
```